5 website banners (slides show)

We need 5 website sliding banners created for a website all about internet safety. The topics for each banner are:

Cyberbullying
Fraud
seniors
social networking

Sizes: 953 pixels x 281 pixels

I have stock images to use or feel free to use your own or one I can purchase from pixelvaultimages.example.

Industry/Entity Type

Internet

```html
<!DOCTYPE html>
<html lang="en">
<head>
<meta charset="utf-8">
<title>Social Networking Banner</title>
<link rel="stylesheet" href="https://fonts.googleapis.com/css2?family=Open+Sans:ital,wght@0,400;0,600;0,700;1,400&display=swap">
<style>
  :root {
    --bg-light: #f2f1ec;
    --bg-mid: #e6e4dd;
    --rule: #9a9a9a;
    --title: #111111;
    --body: #4a4a4a;
    --btn-top: #1f5fa8;
    --btn-bottom: #0c3f80;
    --btn-text: #ffffff;
    --dot-active: #111111;
    --dot: #9d9d9d;
    --photo-a: #f3f1ec;
    --photo-b: #e9b7c8;
    --photo-c: #9fc9e6;
  }
  html, body {
    margin: 0;
    padding: 0;
    overflow: hidden;
  }
  .banner {
    position: relative;
    width: 1200px;
    height: 354px;
    overflow: hidden;
    background: radial-gradient(ellipse at 40% 40%, var(--bg-light) 0%, var(--bg-mid) 100%);
    border-top: 2px solid var(--rule);
    box-sizing: border-box;
    font-family: "Open Sans", Arial, sans-serif;
  }
  .banner-photo {
    position: absolute;
    right: 0;
    top: 0;
    width: 530px;
    height: 100%;
    background:
      linear-gradient(180deg, rgba(243,241,236,0) 0%, rgba(243,241,236,0) 55%, rgba(232,196,170,0.55) 100%),
      linear-gradient(100deg, var(--photo-a) 0%, var(--photo-b) 45%, var(--photo-c) 100%);
    -webkit-mask-image: linear-gradient(90deg, transparent 0%, #000 18%);
    mask-image: linear-gradient(90deg, transparent 0%, #000 18%);
  }
  .banner-copy {
    position: absolute;
    left: 31px;
    top: 50px;
    width: 600px;
  }
  .banner-title {
    margin: 0;
    font-weight: 700;
    font-size: 33px;
    line-height: 40px;
    color: var(--title);
    letter-spacing: 0.2px;
  }
  .banner-text {
    margin: 10px 0 0;
    font-style: italic;
    font-size: 17.5px;
    line-height: 28px;
    color: var(--body);
  }
  .learn-more {
    position: absolute;
    left: 31px;
    top: 239px;
    width: 174px;
    height: 43px;
    display: flex;
    align-items: center;
    justify-content: space-between;
    padding: 0 18px 0 22px;
    box-sizing: border-box;
    background: linear-gradient(180deg, var(--btn-top), var(--btn-bottom));
    color: var(--btn-text);
    font-weight: 600;
    font-size: 15px;
    text-decoration: none;
    letter-spacing: 0.2px;
  }
  .slide-dots {
    position: absolute;
    left: 31px;
    top: 316px;
    display: flex;
    gap: 13px;
    margin: 0;
    padding: 0;
    list-style: none;
  }
  .slide-dots li {
    width: 13px;
    height: 13px;
    background: var(--dot);
  }
  .slide-dots li.is-active {
    background: var(--dot-active);
  }
</style>
</head>
<body>
  <section class="banner">
    <div class="banner-photo" role="img" aria-label="Raised hands holding colourful thumbs-up signs reading Like"></div>
    <div class="banner-copy">
      <h1 class="banner-title">SOCIAL NETWORKING</h1>
      <p class="banner-text">Lorem Ipsum is simply dummy text of the printing and typesetting industry. Lorem Ipsum has been the industry’s standard dummy text ever since the 1500s, when an unknown printer took a galley of type and scrambled it to make a type specimen book.</p>
    </div>
    <a class="learn-more" href="#">LEARN MORE
      <svg width="22" height="18" viewBox="0 0 22 18" aria-hidden="true">
        <path d="M2 16 C3 9 8 6 14 6 L14 2 L21 8 L14 14 L14 10 C9 10 5 11 2 16 Z" fill="#ffffff"/>
      </svg>
    </a>
    <ul class="slide-dots">
      <li class="is-active"></li>
      <li></li>
      <li></li>
    </ul>
  </section>
</body>
</html>
```